Buch-/eBook-Cover für ein jährlichen Referenzbuchs der Industrie
Zielgruppe
verlag-mentoria ist ein Fachverlag mit Fokus auf Industrie und Technologie. Seit über 30 Jahren entwickeln wir Medienangebote für Technologiemärkte – immer mit dem Ziel, komplexe Inhalte verständlich und ansprechend aufzubereiten.
Unsere Arbeit basiert auf einer echten Begeisterung für Technik. Mit unseren Marken bauen wir Brücken zwischen Anbietern und Anwendern – in Print, digital und auf Events.
Wir veröffentlichen Magazine, organisieren Veranstaltungen und entwickeln für Kunden individuelle Kommunikationskampagnen. Unsere Plattformen sind in ihren Zielbranchen fest etabliert und genießen ein hohes Maß an Vertrauen.
Bei dem ausgeschriebenen Projekt handelt es sich um unser WERKBLICK.next LUMIRANO – Das Referenzbuch der Industrie, welches jährlich erscheint. LUMIRANO ist aus dem polynesischen Sprachraum und steht für Freiraum.
WERKBLICK.next LUMIRANO ist ein Referenzbuch, das den Namen verdient: unkonventionell, hochrelevant, emotional, motivierend. Bewusst umgesetzt als hochwertige Print-Referenzpublikation!
Wandel bestimmt unsere Zeit und verändert unsere Gesellschaft, unsere Unternehmen, uns alle.
Im Wandel liegt Freiraum zur Gestaltung. Gesellschaftlicher Wandel, Technologie-Wandel, Klimawandel, Wertewandel, Führungswandel oder Organisationswandel sind nur einige Beispiele. Wer dabei den Wandel in engen Bahnen denkt, verschenkt Potential. Veränderung braucht Freiraum für neue Ideen und Perspektiven sowie Persönlichkeiten, die diesen nutzen wollen.
Unsere Leserzielgruppe – Vorwärtsdenker und Zukunftsmacher:
Strategische & technische Entscheider in der Industrie: Inhaber, Vorstand, Geschäftsführer, Betriebs- & Werksleiter, Bereichs-, Gruppen-, Abteilungs- und Projektleiter
Redaktionelles Konzept:
Wer gestaltet die Zukunft der Industrie und ihrer Branchen? Und wie?
Wir geben Personen aus der Industrie den Freiraum, ihre P..
Aufgabenstellung
1.) Kurzzusammenfassung der Ausschreibung
Die 6. Ausgabe des jährlichen Referenzbuchs der Industrie, WERKBLICK.next LUMIRANO 2026, erscheint im Oktober 2025. Für das Cover sucht verlag-mentoria neue Vorschläge, die nicht automatisch eine Fortsetzung der vorherigen Titel sind.
2.) Gestalterische & Inhaltliche Anforderungen
• Format: 195x250 mm + 3 mm Anschnitt
• Rücken: ca. 1,3 cm (Stand letzte Publikation 2024)
• Auflösung: Druckqualität, mind. 300 dpi
• Inhaltliche Elemente:
- Cover
LUMIRANO 2026 Schriftzug (Orientierung egal)
{polynesisch: Freiraum}
Untersatz: Das Referenzbuch der Industrie. Für Vorwärtsdenker und Zukunftsmacher.
part of WERKBLICK.next Logo-Balken am unteren Rand (siehe Beispiel-Cover LUMIRANO 2025)
3 Statements (je 100-150 Zeichen mit Leerzeichen), zu verwendende Schrift: Helvetica Neue LT Std
Folgende Statements dienen als Beispiel und müssen im Nachgang noch angepasst werden
ERFOLG DURCH FLEXIBILITÄT: IT-ARCHITEKTUREN UND KI TRANSFORMIEREN UNTERNEHMEN GRUNDLEGEND!
PRODUKTIONSFOOTPRINT DEUTSCHER MITTELSTAND 2030+: REGIONAL, 100 % AUTOMATISIERT, KLIMANEUTRAL!
UNTERNEHMEN, DIE FLEXIBEL UND ADAPTIV SIND, KÖNNEN CHANCEN NUTZEN UND INNOVATIONSFÜHRER BLEIBEN.
- Rücken:
LUMIRANO
Jahreszahl: 2026
Zu verwendende Schrift: Helvetica Neue LT Std
WICHTIG: Die Farbe Orange (0/80/100/0) soll als Wiedererkennung in die Gestaltungen eingebunden werden. Wir geben die Cover der vergangenen Jahre als Beispiel und Orientierung mit, möchten aber abgesehen von der Farbe bewusst in eine neue Richtung gehen. Bei der Orientierung und Platzierung der Schriftzüge gibt es daher keine Vorgaben. Zu den Beispiel-Cover LUMIRANO: https://www.werkblick-verlag.example/de/Lumirano/e-paper
Das Design darf nicht zu überladen sein.

```html
<!DOCTYPE html>
<html lang="de">
<head>
<meta charset="utf-8">
<title>WERKBLICK.next LUMIRANO 2026 – Cover</title>
<link rel="stylesheet" href="https://fonts.googleapis.com/css2?family=Roboto+Condensed:wght@400;500;700&family=Playfair+Display:ital@1&display=swap">
<style>
  :root {
    --orange: #ec4a03;
    --ink: #111111;
    --paper: #ffffff;
    --stage: #f3f4f4;
    --guide: #e04bb0;
    --sans: "Roboto Condensed", "Helvetica Neue", Arial, sans-serif;
    --serif: "Playfair Display", Georgia, serif;
  }
  * { margin: 0; padding: 0; box-sizing: border-box; }
  html, body { width: 1200px; height: 2400px; overflow: hidden; }
  body { background: var(--stage); position: relative; font-family: var(--sans); }

  .sheet { position: absolute; box-shadow: 0 8px 22px rgba(0,0,0,.12); }
  .sheet--front { left: 389px; top: 904px; width: 468px; height: 601px; }
  .sheet--spread { left: 116px; top: 1692px; width: 967px; height: 601px; display: flex; }

  .cover { position: relative; width: 468px; height: 601px; background: var(--orange); overflow: hidden; flex: none; }

  .wordmark, .year { position: absolute; left: 47px; font-weight: 700; font-size: 68px; letter-spacing: -1px; color: var(--ink); white-space: nowrap; }
  .wordmark { top: 66px; line-height: 52px; }
  .year { top: 302px; line-height: 56px; font-size: 70px; }
  .gloss { position: absolute; left: 47px; top: 279px; font-family: var(--serif); font-style: italic; font-size: 11.5px; line-height: 16px; color: var(--ink); white-space: nowrap; }
  .tagline { position: absolute; left: 45px; top: 429px; height: 90px; writing-mode: vertical-rl; transform: rotate(180deg);
             font-family: var(--serif); font-style: italic; font-size: 11.5px; line-height: 15px; text-align: end; white-space: nowrap; color: var(--ink); }

  .cover--back .wordmark, .cover--back .year { left: 355px; }
  .cover--back .gloss { left: auto; right: 44px; }
  .cover--back .tagline { left: 353px; }

  .imprint { position: absolute; left: 0; bottom: 0; width: 100%; height: 23px; background: var(--paper);
             display: flex; align-items: center; justify-content: center; gap: 4px; color: var(--ink); }
  .imprint__pre { font-size: 6px; }
  .imprint__name { font-size: 12px; font-weight: 500; }

  .statement { position: absolute; width: 121px; height: 168px; }
  .statement svg { position: absolute; inset: 0; }
  .statement__mark { position: absolute; left: 0; width: 121px; text-align: center; font-family: Georgia, serif; font-weight: 700; font-size: 24px; line-height: 24px; }
  .statement__text { position: absolute; left: 0; width: 121px; text-align: center; font-size: 9.5px; line-height: 15.4px; white-space: nowrap; }
  .statement--dark { color: var(--paper); }
  .statement--dark .statement__shape { fill: var(--ink); }
  .statement--light { color: var(--ink); }
  .statement--light .statement__shape { fill: var(--paper); }

  .statement--flex { left: 272px; top: 30px; }
  .statement--flex .statement__mark { top: 11px; }
  .statement--flex .statement__text { top: 34px; }
  .statement--footprint { left: 197px; top: 144px; }
  .statement--footprint .statement__mark { top: 8px; }
  .statement--footprint .statement__text { top: 28px; }
  .statement--adaptive { left: 320px; top: 275px; }
  .statement--adaptive .statement__mark { top: 9px; }
  .statement--adaptive .statement__text { top: 29px; }

  .cover--back .statement--flex { left: 77px; }
  .cover--back .statement--footprint { left: 153px; }
  .cover--back .statement--adaptive { left: 32px; }

  .spine { position: relative; width: 31px; height: 601px; background: var(--orange); flex: none; overflow: hidden;
           border-left: 1px dashed var(--guide); border-right: 1px dashed var(--guide); }
  .spine__title { position: absolute; top: 66px; left: 0; width: 100%; text-align: center; font-weight: 700; font-size: 24px; line-height: 21px; letter-spacing: -.5px; color: var(--ink); white-space: nowrap; }
  .spine__year { position: absolute; top: 280px; left: 0; width: 100%; text-align: center; font-weight: 700; font-size: 12px; color: var(--ink); }
  .spine__band { position: absolute; left: 0; bottom: 0; width: 100%; height: 23px; background: var(--paper); }
</style>
</head>
<body>

<section class="sheet sheet--front">
  <div class="cover cover--front">
    <div class="statement statement--dark statement--flex">
      <svg viewBox="0 0 130 180" width="121" height="168"><g class="statement__shape"><circle cx="65" cy="65" r="65"/><path d="M129,74 C127,112 108,146 83,180 L12,180 L42,120 Z"/></g></svg>
      <span class="statement__mark">”</span>
      <p class="statement__text">Erfolg durch Flexibilität:<br>IT-Architekturen und KI<br>transformieren Unternehmen<br>grundlegend!</p>
    </div>
    <div class="statement statement--light statement--footprint">
      <svg viewBox="0 0 130 180" width="121" height="168"><g class="statement__shape"><circle cx="65" cy="65" r="65"/><path d="M129,74 C127,112 108,146 83,180 L12,180 L42,120 Z"/></g></svg>
      <span class="statement__mark">”</span>
      <p class="statement__text">Produktionsfootprint<br>Deutscher Mittelstand 2030+:<br>Regional, 100 % automatisiert,<br>klimaneutral!</p>
    </div>
    <div class="statement statement--dark statement--adaptive">
      <svg viewBox="0 0 130 180" width="121" height="168"><g class="statement__shape"><circle cx="65" cy="65" r="65"/><path d="M129,74 C127,112 108,146 83,180 L12,180 L42,120 Z"/></g></svg>
      <span class="statement__mark">”</span>
      <p class="statement__text">Unternehmen,<br>die Flexibel und adaptiv<br>sind, können Chancen nutzen<br>und Innovationsführer<br>bleiben.</p>
    </div>

    <h1 class="wordmark">LU<br>MI<br>RA<br>NO</h1>
    <p class="gloss">{polynesisch: Freiraum}</p>
    <p class="year">20<br>26</p>
    <p class="tagline">Das Referenzbuch<br>der Industrie.<br>Für Vorwärts-<br>denker und<br>Zukunftsmacher.</p>

    <footer class="imprint"><span class="imprint__pre">part of</span><span class="imprint__name">WERKBLICK.next</span></footer>
  </div>
</section>

<section class="sheet sheet--spread">
  <div class="cover cover--back">
    <div class="statement statement--dark statement--flex">
      <svg viewBox="0 0 130 180" width="121" height="168"><g class="statement__shape"><circle cx="65" cy="65" r="65"/><path d="M129,74 C127,112 108,146 83,180 L12,180 L42,120 Z"/></g></svg>
      <span class="statement__mark">”</span>
      <p class="statement__text">Erfolg durch Flexibilität:<br>IT-Architekturen und KI<br>transformieren Unternehmen<br>grundlegend!</p>
    </div>
    <div class="statement statement--light statement--footprint">
      <svg viewBox="0 0 130 180" width="121" height="168"><g class="statement__shape"><circle cx="65" cy="65" r="65"/><path d="M129,74 C127,112 108,146 83,180 L12,180 L42,120 Z"/></g></svg>
      <span class="statement__mark">”</span>
      <p class="statement__text">Produktionsfootprint<br>Deutscher Mittelstand 2030+:<br>Regional, 100 % automatisiert,<br>klimaneutral!</p>
    </div>
    <div class="statement statement--dark statement--adaptive">
      <svg viewBox="0 0 130 180" width="121" height="168"><g class="statement__shape"><circle cx="65" cy="65" r="65"/><path d="M129,74 C127,112 108,146 83,180 L12,180 L42,120 Z"/></g></svg>
      <span class="statement__mark">”</span>
      <p class="statement__text">Unternehmen,<br>die Flexibel und adaptiv<br>sind, können Chancen nutzen<br>und Innovationsführer<br>bleiben.</p>
    </div>

    <p class="wordmark">LU<br>MI<br>RA<br>NO</p>
    <p class="gloss">{polynesisch: Freiraum}</p>
    <p class="year">20<br>26</p>
    <p class="tagline">Das Referenzbuch<br>der Industrie.<br>Für Vorwärts-<br>denker und<br>Zukunftsmacher.</p>

    <footer class="imprint"><span class="imprint__pre">part of</span><span class="imprint__name">WERKBLICK.next</span></footer>
  </div>

  <div class="spine">
    <p class="spine__title">LU<br>MI<br>RA<br>NO</p>
    <p class="spine__year">2026</p>
    <div class="spine__band"></div>
  </div>

  <div class="cover cover--front">
    <div class="statement statement--dark statement--flex">
      <svg viewBox="0 0 130 180" width="121" height="168"><g class="statement__shape"><circle cx="65" cy="65" r="65"/><path d="M129,74 C127,112 108,146 83,180 L12,180 L42,120 Z"/></g></svg>
      <span class="statement__mark">”</span>
      <p class="statement__text">Erfolg durch Flexibilität:<br>IT-Architekturen und KI<br>transformieren Unternehmen<br>grundlegend!</p>
    </div>
    <div class="statement statement--light statement--footprint">
      <svg viewBox="0 0 130 180" width="121" height="168"><g class="statement__shape"><circle cx="65" cy="65" r="65"/><path d="M129,74 C127,112 108,146 83,180 L12,180 L42,120 Z"/></g></svg>
      <span class="statement__mark">”</span>
      <p class="statement__text">Produktionsfootprint<br>Deutscher Mittelstand 2030+:<br>Regional, 100 % automatisiert,<br>klimaneutral!</p>
    </div>
    <div class="statement statement--dark statement--adaptive">
      <svg viewBox="0 0 130 180" width="121" height="168"><g class="statement__shape"><circle cx="65" cy="65" r="65"/><path d="M129,74 C127,112 108,146 83,180 L12,180 L42,120 Z"/></g></svg>
      <span class="statement__mark">”</span>
      <p class="statement__text">Unternehmen,<br>die Flexibel und adaptiv<br>sind, können Chancen nutzen<br>und Innovationsführer<br>bleiben.</p>
    </div>

    <p class="wordmark">LU<br>MI<br>RA<br>NO</p>
    <p class="gloss">{polynesisch: Freiraum}</p>
    <p class="year">20<br>26</p>
    <p class="tagline">Das Referenzbuch<br>der Industrie.<br>Für Vorwärts-<br>denker und<br>Zukunftsmacher.</p>

    <footer class="imprint"><span class="imprint__pre">part of</span><span class="imprint__name">WERKBLICK.next</span></footer>
  </div>
</section>

</body>
</html>
```